Flyer für Selbstwert-Coachin und Bewusstseinstrainerin
Der Flyer ist wunderschön, kreativ und edel geworden und wurde von der Designerin genau nach meinen Wünschen super umgesetzt! Ich bin sehr zufrieden und kann die Designerin Lunea2281 jedem nur empfehlen. Einfach Top!!! 1 A!!! Vielen herzlichen Dank!
Zielgruppe
Ich bin Selbstwert Coach und Bewusstseinstrainerin und möchte einen Flyer für mein neues Angebot 'Innenkraft Akademie für Jugendliche ab 16' gestalten lassen.
Die Zielgruppe sind Eltern von Jugendlichen in der Oberstufe, deren Kinder unter Schulstress und Leistungsdruck leiden und zu wenig Selbstbewusstsein haben.
Aufgabenstellung
Ich habe bereits das Titelbild bei Bildquell gesucht #739201584, bitte dieses nehmen, es kann auch ein ähnliches noch besseres vorgeschlagen werden.
Ich möchte einen ansprechenden, schönen, hochwertigen Flyer mit den Farben der Landingpage, gelb, blau, gold... und Bilder von Jugendlichen, dort wo Platz ist, ansprechend und klar. Bitte keine Schnörkel und 08 15 Figuren, das Auge soll hängen bleiben, der Flyer hängt straßenseitig. Dieser soll ein 6-seitiger Wickelfalz sein.

```html
<!DOCTYPE html>
<html lang="de">
<head>
<meta charset="utf-8">
<title>Innenkraft Akademie – Wickelfalz-Flyer</title>
<link href="https://fonts.googleapis.com/css2?family=Oswald:wght@500;700&family=Open+Sans:ital,wght@0,400;0,600;0,700;1,400&display=swap" rel="stylesheet">
<style>
  :root{
    --navy:#1b1b6f;
    --navy-deep:#12124f;
    --yellow:#f2b705;
    --gold-light:#f6e7b0;
    --paper:#ffffff;
    --bg:#c9c9cb;
    --ink:#3a3a48;
    --muted:#6b6b78;
  }
  *{box-sizing:border-box;margin:0;padding:0}
  html,body{width:1200px;height:481px;overflow:hidden;background:var(--bg)}
  body{font-family:"Open Sans",Arial,sans-serif;color:var(--ink);position:relative}
  .sheet{position:absolute;top:38px;width:570px;height:404px;background:var(--paper);display:flex;box-shadow:0 6px 18px rgba(0,0,0,.25)}
  .sheet--inside{left:20px}
  .sheet--outside{left:610px}
  .panel{width:190px;height:100%;position:relative;display:flex;flex-direction:column;overflow:hidden}
  .panel + .panel{border-left:1px solid #ececf0}
  .photo{width:100%;flex:none}
  .headline{font-family:"Oswald",Arial,sans-serif;font-weight:700;text-transform:uppercase;color:var(--navy);line-height:1.05}
  .band{background:var(--navy);color:#fff;font-family:"Oswald",Arial,sans-serif;font-weight:700;text-transform:uppercase;padding:6px 12px;position:relative}
  .band::after{content:"";position:absolute;left:0;right:0;bottom:-3px;height:3px;background:var(--yellow)}
  .band--gold{color:var(--yellow)}
  .copy{font-size:5.6px;line-height:1.5;color:var(--ink)}
  .copy p + p{margin-top:4px}
  .pad{padding:10px 12px}
  .sub{font-family:"Oswald",Arial,sans-serif;font-weight:700;font-size:9px;color:var(--navy);text-transform:uppercase;margin:6px 0 3px}
  .label{font-size:6px;font-weight:700;color:var(--navy);margin:5px 0 2px}
  .bullets{list-style:none;font-size:5.6px;line-height:1.5}
  .bullets li{padding-left:7px;position:relative}
  .bullets li::before{content:"";position:absolute;left:0;top:3px;width:3px;height:3px;border-radius:50%;background:var(--navy)}
  .ticks{list-style:none;font-size:5.6px;line-height:1.5}
  .ticks li{padding-left:9px;position:relative;margin-bottom:1px}
  .ticks svg{position:absolute;left:0;top:1px;width:6px;height:6px}
  .footer{margin-top:auto;background:var(--navy);color:#fff;padding:8px 12px;border-top:3px solid var(--yellow)}
  .footer .sub{color:#fff;margin:0 0 2px}
  .gold-rule{height:4px;background:linear-gradient(90deg,var(--yellow),var(--gold-light))}
  .contact{font-size:5.8px;line-height:1.6}
  .contact strong{font-family:"Oswald",Arial,sans-serif;font-size:9px;color:var(--navy);display:block;margin-bottom:2px}
  .portrait-ring{display:flex;justify-content:center;margin:12px 0 8px}
  .brand{display:flex;align-items:center;gap:5px;justify-content:center;font-family:"Oswald",Arial,sans-serif;font-weight:500;font-size:9px;color:var(--navy)}
  .brand i{width:7px;height:7px;border-radius:50%;background:var(--yellow);display:block}
  .cover-title{font-size:17px;color:#fff;line-height:1}
  .cover-title small{display:block;font-family:"Open Sans",Arial,sans-serif;font-weight:600;font-size:6.5px;text-transform:none;color:var(--yellow);margin-top:3px}
  .cover-lines{font-size:6.5px;line-height:1.7;color:var(--navy);font-weight:600;padding:14px 14px}
  .cover-footer{margin-top:auto;background:var(--navy);color:#fff;font-size:6.5px;line-height:1.5;font-style:italic;padding:12px 14px;border-top:4px solid var(--yellow)}
</style>
</head>
<body>

<!-- Innenseite -->
<section class="sheet sheet--inside" aria-label="Flyer Innenseite">
  <article class="panel panel--intro">
    <div class="pad">
      <h2 class="headline" style="font-size:13px">Hast du das Gefühl,<br>deinem Kind wird<br>alles zu viel?</h2>
      <div class="copy" style="margin-top:7px">
        <p>Schule, Prüfungen und der Blick auf die Zukunft setzen viele Jugendliche unter Druck. Sie zweifeln an sich, ziehen sich zurück und verlieren die Freude am Lernen.</p>
        <p>Als Mutter oder Vater möchtest du helfen, doch oft fehlen die richtigen Worte. Genau hier setzt unser Lehrgang an und begleitet dein Kind Schritt für Schritt.</p>
        <p>Gemeinsam stärken wir Selbstvertrauen, innere Ruhe und die Fähigkeit, Herausforderungen gelassen anzugehen.</p>
      </div>
    </div>
    <svg class="photo" style="margin-top:auto" width="190" height="120" role="img" aria-label="Foto: Jugendliche lachend in einem Sonnenblumenfeld">
      <defs><linearGradient id="sunfield" x1="0" y1="0" x2="0" y2="1"><stop offset="0" stop-color="#e9d27a"/><stop offset="1" stop-color="#b98a14"/></linearGradient></defs>
      <rect width="190" height="120" fill="url(#sunfield)"/>
    </svg>
  </article>

  <article class="panel panel--modules">
    <svg class="photo" width="190" height="92" role="img" aria-label="Foto: grüne Zimmerpflanze in weißem Holzkasten">
      <defs><linearGradient id="plant" x1="0" y1="0" x2="1" y2="1"><stop offset="0" stop-color="#f2f2f2"/><stop offset="1" stop-color="#c7ccc4"/></linearGradient></defs>
      <rect width="190" height="92" fill="url(#plant)"/>
    </svg>
    <div class="band band--gold" style="font-size:14px">20 Module</div>
    <div class="pad" style="padding-top:9px">
      <p class="copy">Der Lehrgang umfasst 20 Module, in denen Jugendliche praxisnahe Werkzeuge für mehr Selbstwert und Gelassenheit im Alltag kennenlernen.</p>
      <div class="sub">Inhalte</div>
      <p class="label">Wie gut kennst du dein Kind?</p>
      <ul class="bullets">
        <li>Stärken entdecken und benennen</li>
        <li>Gefühle verstehen und ausdrücken</li>
        <li>Mit Stress gelassen umgehen</li>
      </ul>
      <p class="label">Glücklich sein, ganz bewusst</p>
      <ul class="bullets">
        <li>Gedanken lenken und Ziele setzen</li>
        <li>Ruheübungen für Prüfungszeiten</li>
        <li>Klare Grenzen freundlich setzen</li>
      </ul>
      <p class="label">Wie stark glaubst du an dich?</p>
      <ul class="bullets">
        <li>Innere Kritik erkennen und wandeln</li>
        <li>Mut für neue Schritte finden</li>
        <li>Erfolge feiern und festhalten</li>
      </ul>
    </div>
  </article>

  <article class="panel panel--coach">
    <svg class="photo" width="190" height="96" role="img" aria-label="Porträtfoto der Coachin">
      <defs><linearGradient id="coach" x1="0" y1="0" x2="1" y2="1"><stop offset="0" stop-color="#d9b783"/><stop offset="1" stop-color="#8b6a4c"/></linearGradient></defs>
      <rect width="190" height="96" fill="url(#coach)"/>
    </svg>
    <div class="band" style="font-size:11px;line-height:1.05">Die Coachin und<br>Vortragende</div>
    <div class="pad" style="padding-top:9px">
      <p class="copy"><strong>Mag. Clara Hofstetter</strong> leitet den schulbegleitenden Lehrgang. Als Selbstwert-Coachin und Bewusstseinstrainerin begleitet sie seit vielen Jahren Jugendliche und Eltern auf dem Weg zu mehr Vertrauen in die eigene Kraft.</p>
      <div class="sub">Termine</div>
      <p class="copy">Der Lehrgang findet wöchentlich statt, jeweils 90 Minuten am späten Nachmittag. Aktuelle Termine und Anmeldung unter <strong style="color:var(--navy)">www.innenkraft-staerken.at/akademie</strong></p>
    </div>
    <div class="footer">
      <div class="sub">Ort</div>
      <p class="copy" style="color:#fff">Der Lehrgang findet online via Videokonferenz statt.</p>
    </div>
  </article>
</section>

<!-- Außenseite -->
<section class="sheet sheet--outside" aria-label="Flyer Außenseite">
  <article class="panel panel--benefits">
    <svg class="photo" width="190" height="70" role="img" aria-label="Foto: Jugendlicher jubelt in heller Küche">
      <defs><linearGradient id="cheer" x1="0" y1="0" x2="1" y2="1"><stop offset="0" stop-color="#e6e4e0"/><stop offset="1" stop-color="#9c8f86"/></linearGradient></defs>
      <rect width="190" height="70" fill="url(#cheer)"/>
    </svg>
    <div class="pad">
      <h2 class="headline" style="font-size:12px;margin-bottom:5px">Vorteile und Nutzen</h2>
      <ul class="ticks">
        <li><svg viewBox="0 0 6 6"><path d="M0.6 3.2 2.3 4.8 5.4 1" fill="none" stroke="#1b1b6f" stroke-width="1.1"/></svg>Mehr Selbstvertrauen in Schule und Alltag</li>
        <li><svg viewBox="0 0 6 6"><path d="M0.6 3.2 2.3 4.8 5.4 1" fill="none" stroke="#1b1b6f" stroke-width="1.1"/></svg>Gelassener Umgang mit Prüfungsangst</li>
        <li><svg viewBox="0 0 6 6"><path d="M0.6 3.2 2.3 4.8 5.4 1" fill="none" stroke="#1b1b6f" stroke-width="1.1"/></svg>Klarheit über eigene Stärken und Ziele</li>
        <li><svg viewBox="0 0 6 6"><path d="M0.6 3.2 2.3 4.8 5.4 1" fill="none" stroke="#1b1b6f" stroke-width="1.1"/></svg>Bessere Konzentration beim Lernen</li>
        <li><svg viewBox="0 0 6 6"><path d="M0.6 3.2 2.3 4.8 5.4 1" fill="none" stroke="#1b1b6f" stroke-width="1.1"/></svg>Übungen, die sofort umsetzbar sind</li>
        <li><svg viewBox="0 0 6 6"><path d="M0.6 3.2 2.3 4.8 5.4 1" fill="none" stroke="#1b1b6f" stroke-width="1.1"/></svg>Mehr Ruhe im Familienleben</li>
        <li><svg viewBox="0 0 6 6"><path d="M0.6 3.2 2.3 4.8 5.4 1" fill="none" stroke="#1b1b6f" stroke-width="1.1"/></svg>Freude und Motivation neu entdecken</li>
      </ul>
      <h2 class="headline" style="font-size:11px;margin:10px 0 4px">Voraussetzungen für<br>die Teilnahme</h2>
      <p class="copy">Der Lehrgang richtet sich an Jugendliche ab 16 Jahren. Vorkenntnisse sind nicht nötig, nur die Bereitschaft, sich auf Neues einzulassen und aktiv mitzumachen.</p>
    </div>
  </article>

  <article class="panel panel--contact">
    <svg class="photo" width="190" height="62" role="img" aria-label="Foto: Jugendliche in heller Wohnumgebung">
      <defs><linearGradient id="room" x1="0" y1="0" x2="1" y2="0"><stop offset="0" stop-color="#cfcac4"/><stop offset="1" stop-color="#f1efec"/></linearGradient></defs>
      <rect width="190" height="62" fill="url(#room)"/>
    </svg>
    <div class="band band--gold" style="font-size:10px;line-height:1.1;background:linear-gradient(90deg,var(--navy) 60%,#d9d9ee)">Kontakt &amp;<br>Veranstalterin</div>
    <div class="pad contact" style="padding-top:9px">
      <strong>Mag. Clara Hofstetter</strong>
      Selbstwert-Coach &amp; Bewusstseinstrainerin<br>
      E-Mail: info@innenkraft-staerken.at<br>
      Mobil: +43 (0)660 000 1234
    </div>
    <div class="portrait-ring">
      <svg width="96" height="96" viewBox="0 0 96 96" role="img" aria-label="Runder Porträtausschnitt der Coachin">
        <defs><linearGradient id="round" x1="0" y1="0" x2="1" y2="1"><stop offset="0" stop-color="#e8cf9d"/><stop offset="1" stop-color="#a88a66"/></linearGradient></defs>
        <circle cx="48" cy="48" r="36" fill="url(#round)"/>
        <circle cx="48" cy="48" r="41" fill="none" stroke="var(--navy)" stroke-width="3"/>
        <path d="M48 3 A45 45 0 0 1 93 48" fill="none" stroke="var(--yellow)" stroke-width="3"/>
        <path d="M48 93 A45 45 0 0 1 3 48" fill="none" stroke="var(--yellow)" stroke-width="3"/>
      </svg>
    </div>
    <div class="brand"><i></i>Mag. Clara Hofstetter</div>
    <div class="gold-rule" style="margin-top:auto"></div>
  </article>

  <article class="panel panel--cover">
    <svg class="photo" width="190" height="130" role="img" aria-label="Titelfoto: lachende Jugendliche mit Locken">
      <defs><linearGradient id="girl" x1="0" y1="0" x2="1" y2="1"><stop offset="0" stop-color="#b9a37e"/><stop offset="1" stop-color="#5a4a3a"/></linearGradient></defs>
      <rect width="190" height="130" fill="url(#girl)"/>
    </svg>
    <div class="band" style="padding:9px 14px;border-bottom:4px solid var(--yellow)">
      <h1 class="headline cover-title">Innenkraft<br>Akademie<small>für Jugendliche ab 16</small></h1>
    </div>
    <div class="cover-lines">
      <p>Schulbegleitender Praxis-Lehrgang für mentale Stärke und Selbstbewusstsein</p>
      <p style="margin-top:6px">Schulstress &amp; Leistungsdruck bewältigen</p>
      <p>Selbstsicher, gelassen &amp; angstfrei werden</p>
      <p style="margin-top:6px">und dabei ein starkes Selbstwertgefühl aufbauen und sich selbst vertrauen</p>
    </div>
    <div class="cover-footer">Einfache Übungen, Techniken und Methoden für den Alltag und ein glückliches, erfolgreiches Leben</div>
  </article>
</section>

</body>
</html>
```